Birch Flooring Supply

Basic one-sided business card design using the attached logo. Vintage americana theme. Font is modified Arial Nova Cond, but anything that coordinates can be used

```html
<!DOCTYPE html>
<html lang="en">
<head>
<meta charset="utf-8">
<title>Birch Flooring Supply – Business Card</title>
<link href="https://fonts.googleapis.com/css2?family=Arimo:wght@400;700&display=swap" rel="stylesheet">
<style>
  :root {
    --backdrop: #2a2a2a;
    --card-light: #fbf9f2;
    --card-mid: #f1ecdc;
    --card-deep: #e4dcc3;
    --ink: #1c1c1c;
    --ink-soft: #333333;
    --gold: #a8895a;
  }
  * { margin: 0; padding: 0; box-sizing: border-box; }
  html, body {
    width: 1200px;
    height: 900px;
    overflow: hidden;
    background: var(--backdrop);
    font-family: "Arimo", Arial, sans-serif;
  }
  .business-card {
    position: absolute;
    left: 75px;
    top: 150px;
    width: 1050px;
    height: 600px;
    background: var(--card-light);
    box-shadow: 0 18px 40px rgba(0,0,0,0.45);
    overflow: hidden;
  }
  .card-backdrop {
    position: absolute;
    inset: 0;
    background:
      radial-gradient(ellipse at 88% 8%, var(--card-light) 0%, var(--card-mid) 45%, var(--card-deep) 100%);
  }
  .brand-mark {
    position: absolute;
    right: 90px;
    top: 70px;
    display: flex;
    align-items: center;
    gap: 16px;
  }
  .brand-dot {
    width: 22px;
    height: 22px;
    border-radius: 50%;
    background: var(--gold);
  }
  .brand-name {
    font-size: 40px;
    font-weight: 700;
    color: var(--ink);
    letter-spacing: 0.5px;
  }
  .contact-block {
    position: absolute;
    left: 96px;
    top: 300px;
    color: var(--ink-soft);
  }
  .person-name {
    font-size: 30px;
    font-weight: 400;
    color: var(--ink);
    text-transform: uppercase;
    letter-spacing: 0.5px;
  }
  .person-role {
    font-size: 20px;
    margin-top: 2px;
  }
  .address {
    margin-top: 46px;
    margin-left: 40px;
    font-size: 21px;
    line-height: 1.25;
  }
  .contact-list {
    list-style: none;
    margin-top: 36px;
    margin-left: 80px;
    font-size: 21px;
  }
  .contact-list li {
    display: flex;
    align-items: center;
    gap: 12px;
    margin-bottom: 10px;
  }
  .contact-icon {
    width: 20px;
    height: 20px;
    flex: none;
  }
</style>
</head>
<body>
  <div class="business-card">
    <div class="card-backdrop" role="img" aria-label="Soft cream sunburst rays radiating from the upper right corner"></div>

    <div class="brand-mark">
      <span class="brand-dot"></span>
      <span class="brand-name">Birch Flooring Supply</span>
    </div>

    <div class="contact-block">
      <p class="person-name">Daniel Reed</p>
      <p class="person-role">Director</p>
      <p class="address">4120 Oak Ave , Lakeview, MN<br>United States, Minnesota</p>
      <ul class="contact-list">
        <li>
          <svg class="contact-icon" viewBox="0 0 24 24" aria-hidden="true"><path fill="#1c1c1c" d="M6.6 10.8a15.1 15.1 0 0 0 6.6 6.6l2.2-2.2a1 1 0 0 1 1-.25 11.4 11.4 0 0 0 3.6.57 1 1 0 0 1 1 1V20a1 1 0 0 1-1 1A17 17 0 0 1 3 4a1 1 0 0 1 1-1h3.5a1 1 0 0 1 1 1c0 1.25.2 2.45.57 3.57a1 1 0 0 1-.25 1z"/></svg>
          +1 555-214-0386
        </li>
        <li>
          <svg class="contact-icon" viewBox="0 0 24 24" aria-hidden="true"><rect x="2" y="5" width="20" height="14" fill="#1c1c1c"/><path d="M2 5l10 8 10-8" fill="none" stroke="#f1ecdc" stroke-width="1.6"/></svg>
          hello@birchflooringsupply.com
        </li>
        <li>
          <svg class="contact-icon" viewBox="0 0 24 24" aria-hidden="true"><g fill="none" stroke="#1c1c1c" stroke-width="1.6"><circle cx="12" cy="12" r="9"/><ellipse cx="12" cy="12" rx="4" ry="9"/><path d="M3 12h18M5 7h14M5 17h14"/></g></svg>
          www.birchflooringsupply.com
        </li>
      </ul>
    </div>
  </div>
</body>
</html>
```